Business card for medical clinic

I need an upmarket, modern medical/health business card for my clinic

Contact Information for Business Card

name, address, email, qr code

```html
<!DOCTYPE html>
<html lang="en">
<head>
<meta charset="utf-8">
<title>Kestrel Care Clinic – Business Card</title>
<link rel="stylesheet" href="https://fonts.googleapis.com/css2?family=Crimson+Text:wght@400;600&display=swap">
<style>
  :root {
    --backdrop: #2a2a2c;
    --card-navy: #1c2130;
    --card-navy-deep: #151925;
    --pattern-tone: #262c3d;
    --accent-cyan: #1fa3e0;
    --text-light: #e6e8ee;
    --text-muted: #c9ccd5;
  }
  * { margin: 0; padding: 0; box-sizing: border-box; }
  html, body {
    width: 1200px; height: 852px; overflow: hidden;
    background: var(--backdrop);
    font-family: "Crimson Text", Georgia, serif;
  }
  .stage { position: relative; width: 1200px; height: 852px; }
  .card {
    position: absolute;
    width: 500px; height: 290px;
    border-radius: 22px;
    background: linear-gradient(135deg, var(--card-navy) 0%, var(--card-navy-deep) 100%);
    overflow: hidden;
    top: 281px;
  }
  .card-front { left: 70px; }
  .card-back { left: 630px; }

  /* Front */
  .front-pattern {
    position: absolute; inset: 0;
    background: radial-gradient(circle at 35% 40%, var(--pattern-tone) 0%, var(--card-navy-deep) 75%);
  }
  .brand {
    display: flex; align-items: center; gap: 8px;
    color: var(--accent-cyan);
    font-weight: 600;
    letter-spacing: 0.03em;
    text-transform: uppercase;
    white-space: nowrap;
  }
  .brand-dot {
    width: 12px; height: 12px; border-radius: 50%;
    background: var(--accent-cyan);
    flex: none;
  }
  .card-front .brand {
    position: absolute; left: 50%; top: 50%;
    transform: translate(-50%, -50%);
    font-size: 24px;
  }

  /* Back */
  .card-back .brand {
    position: absolute; left: 32px; top: 52px;
    font-size: 16px;
  }
  .contact-list {
    position: absolute; left: 286px; top: 48px;
    list-style: none;
    color: var(--text-light);
    font-size: 13px; line-height: 1.45;
    white-space: nowrap;
  }
  .contact-list li { display: flex; align-items: center; gap: 8px; }
  .contact-icon { width: 11px; height: 11px; flex: none; }
  .contact-address { margin-top: 6px; }
  .person { position: absolute; left: 32px; bottom: 40px; }
  .person-name {
    color: var(--accent-cyan);
    font-size: 24px; font-weight: 400;
    letter-spacing: 0.04em; text-transform: uppercase;
    line-height: 1.1;
  }
  .person-role { color: var(--text-light); font-size: 15px; }
</style>
</head>
<body>
<main class="stage">
  <section class="card card-front">
    <div class="front-pattern" role="img" aria-label="Embossed pattern of rings across the card face"></div>
    <div class="brand"><span class="brand-dot"></span>Kestrel Care Clinic</div>
  </section>

  <section class="card card-back">
    <div class="brand"><span class="brand-dot"></span>Kestrel Care Clinic</div>

    <ul class="contact-list">
      <li>
        <svg class="contact-icon" viewBox="0 0 12 12"><rect x="0" y="0" width="12" height="12" rx="2" fill="var(--accent-cyan)"/><path d="M3.5 3 L5 3 L5.6 4.6 L4.8 5.2 Q5.6 6.6 6.8 7.2 L7.4 6.4 L9 7 L9 8.5 Q5 9 3 4.5 Z" fill="var(--card-navy)"/></svg>
        0700-555-01234
      </li>
      <li>
        <svg class="contact-icon" viewBox="0 0 12 12"><rect x="0" y="0" width="12" height="12" rx="2" fill="var(--accent-cyan)"/><rect x="2.5" y="3.5" width="7" height="5" fill="none" stroke="var(--card-navy)" stroke-width="1"/><path d="M2.5 3.5 L6 6.3 L9.5 3.5" fill="none" stroke="var(--card-navy)" stroke-width="1"/></svg>
        hello@kestrelcare.example
      </li>
      <li>
        <svg class="contact-icon" viewBox="0 0 12 12"><circle cx="6" cy="6" r="6" fill="var(--accent-cyan)"/><circle cx="6" cy="6" r="3.6" fill="none" stroke="var(--card-navy)" stroke-width="0.9"/><path d="M2.4 6 H9.6 M6 2.4 V9.6" stroke="var(--card-navy)" stroke-width="0.9"/></svg>
        www.kestrelcare.example
      </li>
      <li class="contact-address">18 Harbour Ln, Westfield, US 40021</li>
    </ul>

    <div class="person">
      <h1 class="person-name">Elena Marsh</h1>
      <p class="person-role">Managing Director</p>
    </div>
  </section>
</main>
</body>
</html>
```